Pemberton Dialworks Business Card Design

Double Sided Business Card Design for a Locksmith company specializing in Safecracking, safe & vault service.

```html
<!DOCTYPE html>
<html lang="en">
<head>
<meta charset="UTF-8">
<title>Pemberton Dialworks Business Card</title>
<link href="https://fonts.googleapis.com/css2?family=Montserrat:wght@400;500;600;800&display=swap" rel="stylesheet">
<style>
  :root {
    --brand-green: #1f7a3a;
    --ink: #1d1d1d;
    --text-grey: #3a3a3a;
    --card-white: #ffffff;
    --backdrop: #e6e8ea;
  }
  * { box-sizing: border-box; margin: 0; padding: 0; }
  html, body {
    width: 1200px; height: 900px; overflow: hidden;
    background: var(--backdrop);
    font-family: "Montserrat", Arial, sans-serif;
  }
  .sheet {
    width: 1200px; height: 900px;
    display: flex; flex-direction: column;
    align-items: center; justify-content: center; gap: 56px;
  }
  .card {
    width: 600px; height: 343px;
    background: var(--card-white);
    border-radius: 22px;
    box-shadow: 0 10px 28px rgba(0,0,0,0.14);
    position: relative; overflow: hidden;
  }
  .brand {
    display: flex; align-items: center; gap: 14px;
  }
  .brand-dot {
    width: 40px; height: 40px; border-radius: 50%;
    background: var(--brand-green); flex: none;
  }
  .brand-name {
    font-weight: 800; color: var(--brand-green);
    text-transform: uppercase; line-height: 1.05;
    letter-spacing: 0.5px;
  }
  /* back side */
  .card--back { display: flex; align-items: center; justify-content: center; }
  .card--back .brand-name { font-size: 34px; }
  .card--back .brand-dot { width: 58px; height: 58px; }
  /* front side */
  .card--front { display: flex; align-items: center; padding: 0 36px; }
  .front-brand { width: 250px; }
  .front-brand .brand-name { font-size: 22px; }
  .divider {
    width: 2px; height: 190px; background: var(--brand-green);
    margin: 0 28px 0 8px; flex: none;
  }
  .contact { color: var(--text-grey); }
  .contact-name { font-size: 21px; font-weight: 600; color: var(--brand-green); }
  .contact-title { font-size: 15px; font-weight: 400; margin-bottom: 12px; }
  .contact-address { font-size: 11.5px; line-height: 1.5; margin-bottom: 10px; }
  .contact-row {
    display: flex; align-items: center; gap: 9px;
    font-size: 11.5px; line-height: 1.9;
  }
  .contact-row svg { width: 14px; height: 14px; fill: none; stroke: var(--brand-green); stroke-width: 2; flex: none; }
  .contact-row svg.solid { fill: var(--brand-green); stroke: none; }
</style>
</head>
<body>
<main class="sheet">
  <section class="card card--back" aria-label="Card back">
    <div class="brand">
      <span class="brand-dot"></span>
      <span class="brand-name">Pemberton<br>Dialworks</span>
    </div>
  </section>

  <section class="card card--front" aria-label="Card front">
    <div class="brand front-brand">
      <span class="brand-dot"></span>
      <span class="brand-name">Pemberton<br>Dialworks</span>
    </div>
    <span class="divider"></span>
    <div class="contact">
      <p class="contact-name">Marcus Holloway</p>
      <p class="contact-title">President</p>
      <p class="contact-address">418 Alder Grove Rd,<br>Suite 210 Brookfield, TX 75480</p>
      <p class="contact-row">
        <svg class="solid" viewBox="0 0 24 24"><path d="M6.6 10.8a15.1 15.1 0 0 0 6.6 6.6l2.2-2.2c.3-.3.7-.4 1-.2 1.1.4 2.3.6 3.6.6.6 0 1 .4 1 1V20c0 .6-.4 1-1 1A17 17 0 0 1 3 4c0-.6.4-1 1-1h3.5c.6 0 1 .4 1 1 0 1.3.2 2.5.6 3.6.1.3 0 .7-.2 1z"/></svg>
        555-214-0937
      </p>
      <p class="contact-row">
        <svg viewBox="0 0 24 24"><rect x="3" y="5" width="18" height="14" rx="1"/><path d="M3 6l9 7 9-7"/></svg>
        info@pembertondialworks.com
      </p>
      <p class="contact-row">
        <svg viewBox="0 0 24 24"><circle cx="12" cy="12" r="9"/><path d="M3 12h18M12 3c3 3 3 15 0 18M12 3c-3 3-3 15 0 18"/></svg>
        www.pembertondialworks.com
      </p>
    </div>
  </section>
</main>
</body>
</html>
```